Bright Dabs - Face Painting Company requires business card design

Hi,
I am wanting a business card design for a new business in Brisbane (Australia) called 'Bright Dabs'. We are a childrens face painting company.

I want to communicate a corporate, simple and clean message through my business card, but also fun and relevant to children.

My company colours are black, yellow and purple, and at the moment I am running with a "cheeky smile" type theme, along the lines of the Marchwood Fox (Tobin in Farrowvale).

I want this to look Corporate, clean and simple. On the back I would like to see some creative flair with a border or background design, perhaps in white or another colour.

Requirements
Must have
• Front:
Bright Dabs
Face Painting Designs

Back:
Maren Lockwell
Artist
0491 283 516
maren@brightdabs.com.au
www.brightdabs.com.au
Nice to have
• Attached is the banner which i had made, the business card should go along with this type of theme.
I would like to use the colours Yellow, Black and Purple. Purple should be used in a miniml way, with yellow and black as the main colours.
I want it to have a CORPORATE look.

A Playfull but readable text.

I would like a mix up of the colours on the back in the text.
Maren Lockwell (black)
Artist(purple) etc.

```html
<!DOCTYPE html>
<html lang="en">
<head>
<meta charset="utf-8">
<title>Bright Dabs – Business Cards</title>
<link rel="stylesheet" href="https://fonts.googleapis.com/css2?family=Questrial&family=Kaushan+Script&display=swap">
<style>
  :root {
    --backdrop: #d49a4e;
    --brand-yellow: #f2ec50;
    --pale-yellow: #f7f1a8;
    --card-white: #ffffff;
    --ink: #111111;
    --brand-purple: #7a3e96;
    --on-purple: #ffffff;
  }
  html, body {
    margin: 0;
    padding: 0;
    overflow: hidden;
  }
  .sheet {
    position: relative;
    width: 1200px;
    height: 780px;
    background: var(--backdrop);
    overflow: hidden;
    font-family: "Questrial", "Century Gothic", sans-serif;
  }
  .card {
    position: absolute;
    width: 488px;
    height: 298px;
    overflow: hidden;
  }
  .card--front {
    left: 358px;
    top: 36px;
    height: 296px;
    background: var(--brand-yellow);
  }
  .card--back {
    top: 420px;
    background: var(--card-white);
  }
  .card--back-purple { left: 62px; }
  .card--back-yellow { left: 652px; }

  .front-ornament {
    position: absolute;
    right: 0;
    top: 0;
    width: 260px;
    height: 296px;
    background: radial-gradient(ellipse at 75% 55%, rgba(255,255,255,0.75) 0%, rgba(255,255,255,0.25) 45%, rgba(255,255,255,0) 75%);
  }
  .back-ornament {
    position: absolute;
    inset: 0;
    background:
      radial-gradient(ellipse at 10% 15%, rgba(247,241,168,0.9) 0%, rgba(247,241,168,0) 40%),
      radial-gradient(ellipse at 45% 95%, rgba(247,241,168,0.95) 0%, rgba(247,241,168,0) 55%),
      radial-gradient(ellipse at 85% 20%, rgba(247,241,168,0.5) 0%, rgba(247,241,168,0) 40%);
  }

  .brand-name {
    position: absolute;
    left: 0;
    right: 0;
    top: 98px;
    margin: 0;
    text-align: center;
    font-size: 58px;
    font-weight: 400;
    letter-spacing: 1px;
    color: var(--ink);
    text-transform: uppercase;
  }
  .brand-tagline {
    position: absolute;
    left: 90px;
    top: 168px;
    margin: 0;
    font-size: 27px;
    color: var(--ink);
    letter-spacing: 0.5px;
  }

  .artist-name {
    position: absolute;
    left: 25px;
    top: 98px;
    margin: 0;
    font-size: 36px;
    font-weight: 400;
    color: var(--ink);
  }
  .artist-role {
    position: absolute;
    left: 36px;
    top: 132px;
    margin: 0;
    font-family: "Kaushan Script", cursive;
    font-size: 40px;
    color: var(--brand-purple);
  }
  .contact {
    position: absolute;
    right: 0;
    width: 186px;
    padding: 7px 0 7px 8px;
    margin: 0;
    list-style: none;
    font-size: 14px;
    line-height: 18px;
  }
  .contact--purple {
    top: 112px;
    background: var(--brand-purple);
    color: var(--on-purple);
  }
  .contact--yellow {
    top: 122px;
    background: var(--brand-yellow);
    color: var(--ink);
  }
  .contact .phone { font-size: 16px; }
</style>
</head>
<body>
<main class="sheet">

  <section class="card card--front">
    <div class="front-ornament" role="img" aria-label="Flowing white swirl ornament with dots"></div>
    <h1 class="brand-name">Bright Dabs</h1>
    <p class="brand-tagline">Face Painting Designs</p>
  </section>

  <section class="card card--back card--back-purple">
    <div class="back-ornament" role="img" aria-label="Pale yellow flowing swirl ornament with dots"></div>
    <h2 class="artist-name">Maren Lockwell</h2>
    <p class="artist-role">Artist</p>
    <ul class="contact contact--purple">
      <li class="phone">0491 283 516</li>
      <li>maren@brightdabs.com.au</li>
      <li>www.brightdabs.com.au</li>
    </ul>
  </section>

  <section class="card card--back card--back-yellow">
    <div class="back-ornament" role="img" aria-label="Pale yellow flowing swirl ornament with dots"></div>
    <h2 class="artist-name">Maren Lockwell</h2>
    <p class="artist-role">Artist</p>
    <ul class="contact contact--yellow">
      <li class="phone">0491 283 516</li>
      <li>maren@brightdabs.com.au</li>
      <li>www.brightdabs.com.au</li>
    </ul>
  </section>

</main>
</body>
</html>
```